Flyer / marketing email used to solicate work for specialized tree removal equipment.

I'm looking for a flyer for door to door and direct mail distributon. Please utilize as much of the following verbiage as possible...

Breaking news!¿the only 170' grapple crane in use in North American is coming to your neighborhood This revolutionary technology will be in your area for a limited time. Our equipment allows to us accomplish the most challenging tree scenarios with no climber, limited personnel, and amazing efficiency.

This innovation has completely changed the cost of hazardous removals. Call now to get the most competitive estimate yet.

This technology is so limited and in high demand that it can only be in your area for a short time before it has to move on. Get on the list today, it may be months before it makes another round to your neighborhood. ¿

Target Market(s)

Flyers will be delivered in a high end residential neighborhood. Distribution will be on heavy stock and via email.

Colors

Designer to choose colors to be used in the design.

Requirements
Must have
• My logo. Pictures of the crane equipment. Pictures of other tree equipment.
• I'd like a two sided 4" x 5.5" mailer.
• I have permissions to utilize content from the sample one fold flyers I have uploaded.
• I'd like a majority of the content of the Vortalix (aka. Plover limb sample). The light background of the 842 Boughs sample.
• A "BLACK FRIDAY SALE" theme would be awesome.
Nice to have
• Old time breaking news headline married with a high tech innovative feel
• OR
• BLACK FRIDAY SALE theme.

```html
<!DOCTYPE html>
<html lang="en">
<head>
<meta charset="utf-8">
<title>Grapple Crane Mailer – Round-Clock Arbor</title>
<link href="https://fonts.googleapis.com/css2?family=Barlow:wght@500;600;700;800;900&family=Barlow+Semi+Condensed:wght@700;800&display=swap" rel="stylesheet">
<style>
  :root {
    --backdrop: #bcbdbf;
    --paper: #ffffff;
    --ink: #111111;
    --alert-red: #e0251b;
    --forest: #2f4a1e;
    --sale-yellow: #ffe600;
    --sky-top: #5b8fd8;
    --sky-bottom: #9cc3f2;
  }
  * { margin: 0; padding: 0; box-sizing: border-box; }
  html, body { width: 991px; height: 1200px; overflow: hidden; }
  body { background: var(--backdrop); font-family: "Barlow", sans-serif; color: var(--ink); position: relative; }

  .side { position: absolute; left: 187px; width: 618px; background: var(--paper); overflow: hidden; }
  .side--front { top: 141px; height: 450px; }
  .side--back { top: 610px; height: 449px; }

  /* Front */
  .front-photo {
    position: absolute; left: 282px; top: 0; width: 336px; height: 450px;
    background: linear-gradient(180deg, var(--sky-top) 0%, var(--sky-bottom) 45%, #4f6b3a 75%, #3c4a34 100%);
  }
  .headline-frame {
    position: absolute; left: 13px; top: 16px; width: 318px; height: 390px;
    border: 5px solid var(--ink);
  }
  .headline {
    position: absolute; left: 33px; top: 41px; width: 300px;
    font-weight: 800; font-size: 24.5px; line-height: 23.5px; color: var(--alert-red);
    text-transform: uppercase; letter-spacing: -0.2px;
  }
  .feature-list { position: absolute; left: 53px; top: 153px; list-style: none; }
  .feature-list li {
    display: flex; gap: 4px; font-weight: 700; font-size: 10.8px; line-height: 13.6px;
    margin-bottom: 14px; letter-spacing: -0.15px;
  }
  .feature-list span { width: 185px; }
  .feature-list svg { flex: none; width: 16px; height: 20px; margin-top: 1px; }

  .sale-box {
    position: absolute; left: 72px; top: 300px; width: 200px; height: 128px;
    background: var(--ink); color: var(--paper);
    display: flex; flex-direction: column; align-items: center; justify-content: center;
    text-transform: uppercase; text-align: center;
  }
  .sale-box__kicker { font-weight: 800; font-size: 15px; letter-spacing: 1px; margin-bottom: 4px; }
  .sale-box__title { font-weight: 900; font-size: 31px; line-height: 31px; color: var(--sale-yellow); }

  .front-phone {
    position: absolute; left: 336px; top: 405px; display: flex; align-items: center; gap: 5px;
    color: var(--paper); font-weight: 800; font-size: 32px; letter-spacing: -0.5px;
  }
  .front-phone svg { width: 36px; height: 36px; }
  .brand-name {
    position: absolute; left: 490px; top: 80px; width: 120px; text-align: center;
    font-weight: 700; font-size: 15px; color: var(--forest);
  }
  .brand-name::before {
    content: ""; display: block; width: 14px; height: 14px; margin: 0 auto 4px;
    background: var(--forest); border-radius: 50%;
  }

  /* Back */
  .intro, .urgency {
    position: absolute; left: 19px; width: 352px;
    font-weight: 500; font-size: 12px; line-height: 15.2px;
  }
  .intro { top: 18px; }
  .urgency { top: 146px; }
  .cost-heading {
    position: absolute; left: 19px; top: 94px; width: 350px;
    font-family: "Barlow Semi Condensed", sans-serif; font-weight: 800; font-size: 16px; line-height: 19.5px;
    color: var(--forest); text-transform: uppercase;
  }
  .equipment-photo { position: absolute; top: 214px; height: 144px; }
  .equipment-photo--truck { left: 0; width: 188px; background: linear-gradient(160deg, #8fb3d8 0%, #b9a98a 50%, #4a4f44 100%); }
  .equipment-photo--crane { left: 189px; width: 429px; background: linear-gradient(180deg, #a8c6e6 0%, #6f8a4e 45%, #4a5b3a 100%); }

  .cta-ribbon {
    position: absolute; left: 78px; top: 343px; width: 462px; height: 33px;
    background: var(--forest); clip-path: polygon(4% 0, 100% 0, 96% 100%, 0 100%);
    display: flex; align-items: center; justify-content: center;
    border-top: 3px solid var(--paper);
    font-family: "Barlow Semi Condensed", sans-serif; font-weight: 700; font-size: 15.5px;
    color: var(--paper); text-transform: uppercase;
  }
  .back-phone {
    position: absolute; left: 125px; top: 386px; display: flex; align-items: center; gap: 6px;
    color: var(--forest); font-weight: 800; font-size: 51px; letter-spacing: -1.5px; line-height: 1;
  }
  .back-phone svg { width: 55px; height: 55px; }
</style>
</head>
<body>

<section class="side side--front">
  <div class="front-photo" role="img" aria-label="Blue grapple crane boom reaching up to a tall pine beside a house under a clear sky"></div>
  <div class="brand-name">Round-Clock Arbor</div>

  <div class="headline-frame"></div>
  <h1 class="headline">The only 170' grapple crane in use in North American is coming to your neighborhood</h1>

  <ul class="feature-list">
    <li><svg viewBox="0 0 16 20"><path d="M0 0h16v13l-8 7-8-7z" fill="#111"/><path d="M3.5 8l3.2 3.2 6-6" stroke="#fff" stroke-width="2.2" fill="none"/></svg><span>Carry heavy debris, preserving your property from wear and tear</span></li>
    <li><svg viewBox="0 0 16 20"><path d="M0 0h16v13l-8 7-8-7z" fill="#111"/><path d="M3.5 8l3.2 3.2 6-6" stroke="#fff" stroke-width="2.2" fill="none"/></svg><span>Takedown hazardous trees by remote control without a climber</span></li>
    <li><svg viewBox="0 0 16 20"><path d="M0 0h16v13l-8 7-8-7z" fill="#111"/><path d="M3.5 8l3.2 3.2 6-6" stroke="#fff" stroke-width="2.2" fill="none"/></svg><span>Has remote controlled chainsaw that can cut at high heights without a climber being in danger</span></li>
  </ul>

  <div class="sale-box">
    <span class="sale-box__kicker">Special</span>
    <span class="sale-box__title">Black Friday<br>Sale!</span>
  </div>

  <div class="front-phone">
    <svg viewBox="0 0 40 40"><circle cx="20" cy="20" r="17" fill="none" stroke="#fff" stroke-width="4"/><path d="M13 11c2-1 3 0 4 3s0 3-1 4c1 3 3 5 6 6 1-1 2-2 4-1s4 2 3 4-3 3-5 3c-6-1-12-7-13-13 0-3 1-5 2-6z" fill="#fff"/></svg>
    <span>555.LIMB.900</span>
  </div>
</section>

<section class="side side--back">
  <p class="intro">This revolutionary technology will be in your area for a limited time. Our equipment allows to us accomplish the most challenging tree scenarios with no climber, limited personnel, and amazing efficiency.</p>
  <h2 class="cost-heading">This innovation has completely changed<br>the cost of hazardous removals.</h2>
  <p class="urgency">This technology is so limited and in high demand that it can only be in your area for a short time before it has to move on. Get on the list today, it may be months before it makes another round to your neighborhood.</p>

  <div class="equipment-photo equipment-photo--truck" role="img" aria-label="Bucket truck and crane boom parked beside a house among autumn trees"></div>
  <div class="equipment-photo equipment-photo--crane" role="img" aria-label="Panorama of the grapple crane boom arching over a rooftop in a wooded neighborhood"></div>

  <div class="cta-ribbon">Call now to get the most competitive estimate yet</div>

  <div class="back-phone">
    <svg viewBox="0 0 40 40"><circle cx="20" cy="20" r="17" fill="none" stroke="#2f4a1e" stroke-width="4.5"/><path d="M13 11c2-1 3 0 4 3s0 3-1 4c1 3 3 5 6 6 1-1 2-2 4-1s4 2 3 4-3 3-5 3c-6-1-12-7-13-13 0-3 1-5 2-6z" fill="#2f4a1e"/></svg>
    <span>555.LIMB.900</span>
  </div>
</section>

</body>
</html>
```